【概要】 住宅会社様の完成見学会のバナー制作です。 Web広告で使用するためのバナーデザインを募集します。 【依頼内容】 ・サイズ: 横1200× 縦628px、横1080× 縦1080px ・作成数: 1種類 ・利用用途:SNS広告(facebook/Instagram) 【目的】 完成見学会の来場促進(ぺージは下記) https://harubel.co.jp/ie/news/ie-news-8412-2-2-2-2-3-2-2-2-2-2-2-2/ 【デザインイメージ】 ・ターゲット層:30代~40代前半の主婦(若め)子供ができたばかり。旦那は普通の会社員。 ・雰囲気:お任せします 【使用素材】 添付のものをお使い下さい(全て使用しなくて結構です) ※開催日ですが、11/20.21は終了しているので削除し、残りの日程をバナーに表記してください。 【参考(クライアント)サイト】 https://harubel.co.jp https://sukanemo.com 【契約金額(税抜)】 3,000円/デザイン 最終納品のファイル形式は、AIもしくはPSDデータとしますが、デザイン提出段階では、PDFもしくはJPEGで問題ありません。 その他ご質問等ありましたら、気軽にお問い合わせください。 ご応募をお待ちしております! |

```html
<!DOCTYPE html>
<html lang="ja">
<head>
<meta charset="UTF-8">
<title>harubel 完成見学会</title>
<link rel="stylesheet" href="https://fonts.googleapis.com/css2?family=Jost:wght@200;400&family=Noto+Sans+JP:wght@400;500;700&family=Noto+Serif+JP:wght@500;600&display=swap">
<style>
  :root {
    --ink: #2b2420;
    --brown: #3e2b20;
    --beige: #eee6dc;
    --line: #b9aea3;
    --white: #ffffff;
  }
  * { margin: 0; padding: 0; box-sizing: border-box; }
  html, body { width: 1200px; height: 628px; overflow: hidden; background: var(--white); }
  .banner { position: relative; width: 1200px; height: 628px; overflow: hidden; font-family: "Noto Sans JP", sans-serif; color: var(--ink); }

  .room-photo {
    position: absolute; left: 0; top: 0; width: 620px; height: 628px;
    background:
      linear-gradient(90deg, rgba(250,248,244,0.95) 0%, rgba(240,236,230,0.6) 18%, rgba(0,0,0,0) 34%),
      linear-gradient(180deg, #d9d3ca 0%, #c7bdb0 30%, #8a6a4f 48%, #b78b62 62%, #caa07a 80%, #d3ab84 100%);
  }

  .brand-name { position: absolute; left: 30px; top: 20px; font-family: "Noto Sans JP", sans-serif; font-weight: 500; font-size: 30px; color: var(--ink); letter-spacing: 1px; }

  .event-tag { position: absolute; left: 30px; top: 250px; font-weight: 700; font-size: 27px; color: var(--ink); letter-spacing: 1px; }
  .open-house { position: absolute; left: 26px; top: 300px; font-family: "Jost", sans-serif; font-weight: 200; font-size: 150px; line-height: 150px; color: transparent; -webkit-text-stroke: 2px var(--white); letter-spacing: 6px; }

  .info-panel { position: absolute; left: 620px; top: 0; width: 580px; height: 628px; background: var(--white); }
  .lead { position: absolute; left: 0; width: 580px; top: 70px; text-align: center; font-family: "Noto Serif JP", serif; font-weight: 500; font-size: 34px; letter-spacing: 2px; }
  .headline { position: absolute; left: 0; width: 580px; top: 130px; text-align: center; font-family: "Noto Serif JP", serif; font-weight: 600; font-size: 58px; letter-spacing: 3px; }

  .schedule-label { position: absolute; left: 20px; width: 540px; top: 282px; display: flex; align-items: center; gap: 22px; font-weight: 700; font-size: 22px; letter-spacing: 2px; }
  .schedule-label::before, .schedule-label::after { content: ""; flex: 1; height: 2px; background: var(--line); }

  .dates { position: absolute; left: 30px; top: 336px; display: flex; gap: 0; }
  .date { position: relative; width: 110px; height: 110px; border-radius: 50%; background: var(--beige); }
  .date .month { position: absolute; left: 22px; top: 16px; font-family: "Jost", sans-serif; font-size: 24px; font-weight: 400; }
  .date .slash { position: absolute; left: 45px; top: 22px; width: 2px; height: 40px; background: var(--ink); transform: rotate(28deg); }
  .date .day { position: absolute; left: 49px; top: 30px; font-family: "Jost", sans-serif; font-size: 42px; font-weight: 400; line-height: 1; }
  .date .weekday { position: absolute; left: 0; width: 110px; top: 78px; text-align: center; font-family: "Jost", sans-serif; font-size: 15px; letter-spacing: 1px; }

  .details { position: absolute; left: 50px; top: 492px; display: flex; align-items: center; gap: 12px; font-weight: 700; font-size: 24px; }
  .pill { background: var(--brown); color: var(--white); font-size: 20px; font-weight: 700; padding: 2px 14px; border-radius: 20px; letter-spacing: 2px; }
  .details .value { margin-right: 24px; }

  .cta { position: absolute; left: 0; top: 566px; width: 580px; height: 62px; background: var(--brown); color: var(--white); display: flex; align-items: center; justify-content: center; gap: 18px; font-weight: 500; font-size: 29px; letter-spacing: 2px; }
  .cta svg { width: 20px; height: 24px; }
</style>
</head>
<body>
<div class="banner">
  <div class="room-photo" role="img" aria-label="完成した住宅のリビング。無垢材の床、革のソファ、ペンダントライト、窓辺のレースカーテン"></div>

  <p class="brand-name">harubel</p>

  <p class="event-tag">〈完成見学会・限定開催〉</p>
  <p class="open-house">OPEN<br>HOUSE</p>

  <section class="info-panel">
    <p class="lead">安心の定額制で建てる</p>
    <h1 class="headline">完全自由設計の家</h1>

    <p class="schedule-label">開催情報</p>

    <div class="dates">
      <div class="date"><span class="month">11</span><span class="slash"></span><span class="day">27</span><span class="weekday">SAT</span></div>
      <div class="date"><span class="month">11</span><span class="slash"></span><span class="day">28</span><span class="weekday">SUN</span></div>
      <div class="date"><span class="month">12</span><span class="slash"></span><span class="day">4</span><span class="weekday">SAT</span></div>
      <div class="date"><span class="month">12</span><span class="slash"></span><span class="day">5</span><span class="weekday">SUN</span></div>
    </div>

    <div class="details">
      <span class="pill">時間</span><span class="value">10:00~17:30</span>
      <span class="pill">場所</span><span>富山市赤田</span>
    </div>

    <div class="cta">
      <span>［完全予約制］詳細はコチラ</span>
      <svg viewBox="0 0 20 24" aria-hidden="true"><polygon points="0,0 20,12 0,24" fill="#ffffff"/></svg>
    </div>
  </section>
</div>
</body>
</html>
```